wooden jewelry - pearl necklaces

I sell wooden jeweler (rings and pearls) on markets, and so on. I also opened my business as a carpenter. The rings and a combination of wood and metal. The wood is special wood, not very common on Europe. I paint the rings afterwards. You can see some of the pictures on the pictures I uploaded. The pearls are made of the same kind of wood and colored in all kinds of colors. They are then assembled to bracelets. The jewelry is very individual and looks really cool and all kinds of people.

Target Market(s)

Young urban alternative with a sense of individuality

Contact Information for Business Card

Front:

Text:

„Kugelwerk“ (big)
„Matthias Oberkirch“ (smaler)

Back
„Holzschmuck
Herstellung von individuellem Holz- und Modeschmuck

Matthias Oberkirch
Tel: 015239460518
Lindmayrweg 27
84572 Erlingen

matthiasoberkirch@postfeld.de“

Font styles to use
Sans Serif

Requirements
Nice to have
• Nice to see a camel thorn tree on the background, this is a special wood and some of the rings are made out of this wood.

```html
<!DOCTYPE html>
<html lang="de">
<head>
<meta charset="utf-8">
<title>Kugelwerk – Visitenkarte</title>
<link rel="stylesheet" href="https://fonts.googleapis.com/css2?family=Fira+Sans:wght@800&family=Oswald:wght@500&family=Open+Sans:wght@400&display=swap">
<style>
  :root {
    --bg: #6e6e70;
    --card-dark: #262a31;
    --magenta: #ec1a73;
    --violet: #6a2a9a;
    --white: #ffffff;
    --text-soft: #e6e7ea;
    --bead-cream: #e3cf9a;
    --bead-brown: #7a3f23;
    --bead-plum: #3b1d33;
  }
  html, body {
    margin: 0;
    width: 1200px;
    height: 1200px;
    overflow: hidden;
    background: var(--bg);
  }
  .canvas {
    position: relative;
    width: 1200px;
    height: 1200px;
  }
  .card {
    position: absolute;
    left: 180px;
    width: 840px;
    height: 480px;
    overflow: hidden;
    box-shadow: 0 14px 30px rgba(0,0,0,.35);
  }
  .card--front { top: 70px; }
  .card--back  { top: 640px; background: var(--card-dark); }

  .bead-photo {
    position: absolute;
    inset: 0;
    background:
      radial-gradient(circle at 20% 30%, var(--bead-cream) 0 8%, transparent 20%),
      radial-gradient(circle at 70% 25%, var(--bead-plum) 0 7%, transparent 18%),
      radial-gradient(circle at 40% 80%, var(--bead-brown) 0 9%, transparent 22%),
      radial-gradient(circle at 85% 75%, var(--bead-cream) 0 8%, transparent 20%),
      linear-gradient(135deg, #b88a4e, #5b2e2a 50%, #c9a66a);
  }
  .gradient-band {
    position: absolute;
    background: linear-gradient(90deg, var(--magenta), var(--violet));
    color: var(--white);
    font-family: "Fira Sans", sans-serif;
    font-weight: 800;
    letter-spacing: 2px;
  }
  .brand-band {
    left: 185px;
    top: 215px;
    width: 430px;
    height: 118px;
    border-radius: 10px;
    display: flex;
    flex-direction: column;
    justify-content: center;
    align-items: center;
    font-size: 26px;
    line-height: 1.3;
    white-space: nowrap;
    box-shadow: 0 8px 18px rgba(0,0,0,.35);
  }
  .tagline-band {
    left: 0;
    top: 290px;
    width: 430px;
    height: 142px;
    padding: 0 0 0 34px;
    box-sizing: border-box;
    display: flex;
    flex-direction: column;
    justify-content: center;
    font-size: 21px;
    line-height: 1.35;
    white-space: nowrap;
    box-shadow: 0 8px 18px rgba(0,0,0,.4);
  }
  .contact {
    position: absolute;
    left: 458px;
    top: 150px;
    width: 360px;
    color: var(--text-soft);
    font-family: "Open Sans", sans-serif;
  }
  .contact__name {
    margin: 0 0 6px;
    font-family: "Oswald", sans-serif;
    font-weight: 500;
    font-size: 40px;
    letter-spacing: 1px;
    white-space: nowrap;
    color: var(--white);
  }
  .contact__line {
    display: flex;
    align-items: center;
    gap: 10px;
    font-size: 17px;
    line-height: 1.6;
    white-space: nowrap;
  }
  .contact__icon { width: 14px; height: 14px; fill: var(--magenta); flex: none; }
</style>
</head>
<body>
<div class="canvas">
  <section class="card card--front">
    <div class="bead-photo" role="img" aria-label="Foto bunter Holzperlen in Creme-, Braun-, Rot- und Violetttönen"></div>
    <div class="gradient-band brand-band">
      <span>Kugelwerk (big)</span>
      <span>Matthias Oberkirch (smaler)</span>
    </div>
  </section>

  <section class="card card--back">
    <div class="gradient-band tagline-band">
      <span>Holzschmuck</span>
      <span>Herstellung von individuellem</span>
      <span>Holz- und Modeschmuck.</span>
    </div>
    <div class="contact">
      <h1 class="contact__name">MATTHIAS OBERKIRCH</h1>
      <div class="contact__line">
        <svg class="contact__icon" viewBox="0 0 24 24"><path d="M6.6 10.8a15 15 0 0 0 6.6 6.6l2.2-2.2a1 1 0 0 1 1-.25 11.4 11.4 0 0 0 3.6.57 1 1 0 0 1 1 1V20a1 1 0 0 1-1 1A17 17 0 0 1 3 4a1 1 0 0 1 1-1h3.5a1 1 0 0 1 1 1c0 1.25.2 2.450.57 3.57a1 1 0 0 1-.25 1z"/></svg>
        <span>+0152-3946-0518</span>
      </div>
      <div class="contact__line">
        <svg class="contact__icon" viewBox="0 0 24 24"><path d="M2 5h20v14H2z M2 5l10 8 10-8" stroke="#262a31" stroke-width="1.5"/></svg>
        <span>matthiasoberkirch@postfeld.de</span>
      </div>
      <div class="contact__line">
        <svg class="contact__icon" viewBox="0 0 24 24"><path d="M12 2a7 7 0 0 0-7 7c0 5 7 13 7 13s7-8 7-13a7 7 0 0 0-7-7zm0 9.5A2.5 2.5 0 1 1 12 6.5a2.5 2.5 0 0 1 0 5z"/></svg>
        <span>Lindmayrweg 27 84572 Erlingen</span>
      </div>
    </div>
  </section>
</div>
</body>
</html>
```